VELMIRAN (coffee package design)

Make coffee bag for coffee beans: VELMIRAN is a quality-driven coffee roaster focused on crafting fresh, flavorful coffee from premium beans sourced directly from farms. We build close relationships with growers to ensure ethical practices, traceability, and exceptional quality at the origin. Our small-batch roasting approach brings out the unique character of each bean—highlighting bold notes, rich complexity, and peak freshness. At VELMIRAN, we believe great coffee starts at the source—and ends in your cup, roasted to perfection.

**VELMIRAN** is a quality-driven coffee roaster focused on crafting fresh, flavorful coffee from **premium beans sourced directly from farms**. We build close relationships with growers to ensure ethical practices, traceability, and exceptional quality at the origin. Our small-batch roasting approach brings out the unique character of each bean—highlighting bold notes, rich complexity, and peak freshness. At **VELMIRAN**, we believe great coffee starts at the source—and ends in your cup, roasted to perfection.

VELMIRAN

ETHICALLY SOURCED COFFEE

On Top: 100% Arabica Beans

On Left Side:
Coffee brew guide: https://in.brewboardly.com/pin/318274659201847362/
https://in.brewboardly.com/pin/coffee-brewing-method-chart--207431985562143/

On right side bottom:
STORAGE
Proper storage is essential to maintaining your coffee’s freshness and flavor. Once opened, we recommend keeping your coffee in a cool, dark, dry place and sealed in an airtight container. Always reseal the bag after each use to preserve maximum freshness and aroma.

487 Tullane Street Oakland Ca 94619

Follow Us
www.velmiran.com
Clipreel@velmiran
Pixlo@getvelmiran

Target Market(s)

Coffee/ Cafe

Industry/Entity Type

Coffee

Font styles to use
Other font styles liked:
• Non‑Seasonal Sans

Requirements
Must have
• Clean, modern
Nice to have
• Elegant

```html
<!DOCTYPE html>
<html lang="en">
<head>
<meta charset="utf-8">
<title>VELMIRAN – Coffee Bag Front and Back</title>
<link rel="stylesheet" href="https://fonts.googleapis.com/css2?family=Source+Serif+4:opsz,wght@8..60,400;8..60,600;8..60,700&family=Inter:wght@400&display=swap">
<style>
  :root {
    --page: #ffffff;
    --bag: #f5f3ef;
    --bag-edge: #ebe4dd;
    --ink: #161413;
    --brown: #7a5a45;
    --tan: #b89a84;
    --rule: #cdb5a3;
    --bean-light: #ece6e1;
    --bean-mid: #cfc2ba;
    --caption: #b3b3b3;
  }
  * { box-sizing: border-box; margin: 0; padding: 0; }
  html, body { width: 1200px; height: 675px; overflow: hidden; background: var(--page); }
  .canvas { position: relative; width: 1200px; height: 675px; font-family: "Source Serif 4", Georgia, serif; }

  .bag {
    position: absolute;
    background: linear-gradient(90deg, var(--bag-edge) 0%, var(--bag) 12%, var(--bag) 100%);
    box-shadow: 0 14px 28px rgba(0,0,0,0.06);
  }
  .bag--front { left: 290px; top: 92px; width: 330px; height: 508px; }
  .bag--back { left: 760px; top: 85px; width: 262px; height: 405px; }

  .caption {
    position: absolute;
    font-family: "Inter", Arial, sans-serif;
    font-size: 8px;
    color: var(--caption);
  }
  .caption--front { left: 550px; top: 632px; }
  .caption--back { left: 949px; top: 521px; }

  /* front */
  .front-claim {
    position: absolute; top: 37px; left: 0; width: 100%;
    text-align: center; font-size: 15px; font-weight: 600;
    letter-spacing: 0.06em; color: var(--tan);
  }
  .bean-artwork {
    position: absolute;
    background: radial-gradient(ellipse at 55% 70%, var(--bean-mid) 0%, var(--bean-light) 45%, rgba(236,230,225,0) 75%);
    border-radius: 50% 50% 45% 45%;
  }
  .bag--front .bean-artwork { left: 110px; top: 68px; width: 120px; height: 320px; }
  .wordmark {
    position: absolute; left: 0; width: 100%;
    text-align: center; font-weight: 600; color: var(--ink);
    letter-spacing: -0.02em; line-height: 1;
  }
  .bag--front .wordmark { top: 272px; font-size: 50px; transform: scaleX(0.84); }
  .tagline {
    position: absolute; left: 0; width: 100%;
    text-align: center; font-weight: 600; color: var(--brown);
    letter-spacing: 0.08em;
  }
  .bag--front .tagline { top: 321px; font-size: 10px; }
  .front-rule { position: absolute; left: 38px; right: 32px; top: 436px; border-top: 1px solid var(--rule); }
  .net-weight { position: absolute; right: 52px; top: 444px; font-size: 13px; font-weight: 700; color: var(--tan); }

  /* back */
  .bag--back .bean-artwork { left: 108px; top: 25px; width: 50px; height: 105px; }
  .bag--back .wordmark { top: 80px; font-size: 27px; transform: scaleX(0.86); }
  .bag--back .tagline { top: 109px; font-size: 5.5px; }
  .back-rule { position: absolute; left: 22px; right: 30px; border-top: 0.6px solid var(--rule); }
  .back-rule--top { top: 137px; }
  .back-rule--bottom { top: 268px; }
  .brand-story {
    position: absolute; left: 48px; width: 164px; top: 158px;
    text-align: center; font-size: 6.6px; line-height: 8.45px; color: var(--brown);
    font-weight: 400;
  }
  .brand-story strong { color: var(--ink); font-weight: 600; }
  .storage { position: absolute; left: 26px; top: 288px; width: 96px; color: var(--tan); }
  .storage h2 { font-size: 4.8px; font-weight: 400; letter-spacing: 0.05em; margin-bottom: 1px; }
  .storage p { font-size: 4.1px; line-height: 6.1px; }
  .contact { position: absolute; right: 40px; top: 302px; text-align: right; font-size: 3.6px; line-height: 5px; color: var(--tan); }
  .contact .address { margin-bottom: 4px; }
  .brew-guide { position: absolute; left: 26px; top: 356px; font-size: 4.6px; line-height: 6.2px; color: var(--tan); }
  .brew-guide h2 { font-size: 5px; font-weight: 700; margin-bottom: 1px; }
</style>
</head>
<body>
<main class="canvas">

  <section class="bag bag--front" aria-label="Bag front">
    <p class="front-claim">100% Arabica Beans</p>
    <div class="bean-artwork" role="img" aria-label="Illustration of coffee beans rising in a curving stream"></div>
    <h1 class="wordmark">VELMIRAN</h1>
    <p class="tagline">ETHICALLY SOURCED COFFEE</p>
    <div class="front-rule"></div>
    <p class="net-weight">250g</p>
  </section>
  <span class="caption caption--front">Front</span>

  <section class="bag bag--back" aria-label="Bag back">
    <div class="bean-artwork" role="img" aria-label="Illustration of coffee beans rising in a curving stream"></div>
    <p class="wordmark">VELMIRAN</p>
    <p class="tagline">ETHICALLY SOURCED COFFEE</p>
    <div class="back-rule back-rule--top"></div>
    <p class="brand-story"><strong>VELMIRAN</strong> is a quality-driven coffee roaster focused on crafting fresh, flavorful coffee from <strong>premium beans sourced directly from farms</strong>. We build close relationships with growers to ensure ethical practices, traceability, and exceptional quality at the origin. Our small-batch roasting approach brings out the unique character of each bean—highlighting bold notes, rich complexity, and peak freshness. At <strong>VELMIRAN</strong>, we believe great coffee starts at the source—and ends in your cup, roasted to perfection.</p>
    <div class="back-rule back-rule--bottom"></div>
    <div class="storage">
      <h2>STORAGE</h2>
      <p>Proper storage is essential to maintaining your coffee’s freshness and flavor. Once opened, we recommend keeping your coffee in a cool, dark, dry place and sealed in an airtight container. Always reseal the bag after each use to preserve maximum freshness and aroma.</p>
    </div>
    <div class="contact">
      <p class="address">487 Tullane Street Oakland Ca 94619</p>
      <p>Follow Us</p>
      <p>www.velmiran.com</p>
      <p>Clipreel@velmiran</p>
      <p>Pixlo@getvelmiran</p>
    </div>
    <div class="brew-guide">
      <h2>Coffee brew guide:</h2>
      <p>https://in.brewboardly.com/pin/318274659201847362/</p>
      <p>https://in.brewboardly.com/pin/coffee-brewing-method-chart--207431985562143/</p>
    </div>
  </section>
  <span class="caption caption--back">Back</span>

</main>
</body>
</html>
```